Need a sleek, professional business card design for a Web Development business

I need a unique business card designed for a web development company. It is also the parent company for any ventures I do, such as my ClipWave channel, startup ideas I have, etc. I am the single member of "Bright Harbor Code LLC." I will attach my basic logo here, so you will see the current color scheme and have the asset available. Thank you!

Target Market(s)

Startups, SMB's, Professionals

Industry/Entity Type

Business

Font styles to use
Other font styles liked:
• Lovello for headings is what I use, but not necessary.

Colors

Designer to choose colors to be used in the design.

Requirements
Nice to have
• Sleek is the word. Professional, modern, dark.
Should not have
• Any work from someone else's design. Lacking originality.

```html
<!DOCTYPE html>
<html lang="en">
<head>
<meta charset="UTF-8">
<title>Bright Harbor Code LLC — Business Card</title>
<link rel="stylesheet" href="https://fonts.googleapis.com/css2?family=Montserrat:wght@500;600;800;900&family=Source+Code+Pro:wght@400&display=swap">
<style>
  :root {
    --bg: #d8d5d2;
    --card-dark: #232323;
    --band: #000000;
    --ink: #111111;
    --coral: #ee6470;
    --peach: #f8a05c;
    --orange: #f79a5a;
    --tag: rgba(255, 255, 255, 0.45);
  }
  * { margin: 0; padding: 0; box-sizing: border-box; }
  html, body { width: 1200px; height: 1200px; overflow: hidden; }
  body {
    background: var(--bg);
    font-family: "Montserrat", Arial, sans-serif;
    position: relative;
  }
  .card {
    position: absolute;
    top: 330px;
    width: 540px;
    height: 540px;
    border-radius: 28px;
    overflow: hidden;
    box-shadow: 0 18px 40px rgba(0,0,0,0.25);
  }
  .card--front { left: 45px; background: var(--card-dark); }
  .card--back {
    left: 615px;
    background: linear-gradient(35deg, var(--peach) 0%, #f4836a 55%, var(--coral) 100%);
  }

  /* Front: brand name */
  .front-brand {
    position: absolute;
    inset: 0;
    display: flex;
    align-items: center;
    justify-content: center;
    gap: 18px;
  }
  .front-brand__dot {
    width: 34px; height: 34px; border-radius: 50%;
    background: var(--orange);
  }
  .front-brand__name {
    color: var(--orange);
    font-weight: 800;
    font-size: 34px;
    line-height: 1.15;
  }

  /* Back: portrait area */
  .portrait {
    position: absolute;
    left: 0; top: 0;
    width: 280px; height: 442px;
    background: radial-gradient(ellipse at 45% 45%, rgba(255,200,160,0.45) 0%, rgba(248,160,92,0.0) 70%);
  }

  .line { position: absolute; white-space: nowrap; color: var(--ink); }
  .tag {
    font-family: "Source Code Pro", monospace;
    font-size: 11px;
    color: var(--tag);
    font-weight: 400;
    margin-left: 6px;
  }
  .tag--lead { margin-left: 0; margin-right: 6px; }
  .name { left: 49px; top: 86px; font-weight: 900; font-size: 34px; }
  .role { left: 89px; top: 130px; font-weight: 600; font-size: 22px; }
  .company { left: 131px; top: 166px; font-weight: 500; font-size: 22px; }
  .services-title { left: 215px; top: 202px; font-weight: 800; font-size: 18px; }
  .service { left: 260px; font-weight: 500; font-size: 17px; }
  .service--1 { top: 243px; }
  .service--2 { top: 271px; }
  .service--3 { top: 298px; }
  .contact { left: 215px; font-weight: 800; font-size: 14px; }
  .contact--phone { top: 358px; }
  .contact--email { top: 386px; font-size: 13px; }
  .contact--web { top: 411px; font-size: 13px; }

  .band {
    position: absolute;
    left: 0; right: 0; bottom: 0;
    height: 98px;
    background: var(--band);
  }
  .badge {
    position: absolute;
    left: 23px; top: 402px;
    width: 116px; height: 116px;
    border-radius: 6px;
    background: var(--card-dark);
    display: flex;
    align-items: center;
    justify-content: center;
    text-align: center;
    padding: 8px;
  }
  .badge__name {
    color: var(--orange);
    font-weight: 800;
    font-size: 15px;
    line-height: 1.2;
  }
</style>
</head>
<body>
  <section class="card card--front" aria-label="Card front">
    <div class="front-brand">
      <span class="front-brand__dot"></span>
      <span class="front-brand__name">Bright Harbor<br>Code</span>
    </div>
  </section>

  <section class="card card--back" aria-label="Card back">
    <div class="portrait" role="img" aria-label="Portrait photo of the founder, tinted in peach tones"></div>

    <p class="line name"><span class="tag tag--lead">&lt;h1&gt;</span>Declan Whitmore<span class="tag">&lt;/h1&gt;</span></p>
    <p class="line role"><span class="tag tag--lead">&lt;h2&gt;</span>Founder, CEO<span class="tag">&lt;/h2&gt;</span></p>
    <p class="line company">Bright Harbor Code LLC.<span class="tag">&lt;/h3&gt;</span></p>
    <p class="line services-title">Services offered<span class="tag">&lt;/strong&gt;&lt;/p&gt;</span></p>
    <p class="line service service--1">Web development<span class="tag">&lt;/li&gt;</span></p>
    <p class="line service service--2">Start-up ideas<span class="tag">&lt;/li&gt;</span></p>
    <p class="line service service--3">Trainings and Tutorials<span class="tag">&lt;/li&gt;</span></p>
    <p class="line contact contact--phone">(555) 010 2468<span class="tag">&lt;br&gt;</span></p>
    <p class="line contact contact--email">d.whitmore@brightharborcode.com<span class="tag">&lt;br&gt;</span></p>
    <p class="line contact contact--web">www.brightharborcode.com<span class="tag">&lt;/strong&gt;</span></p>

    <div class="band"></div>
    <div class="badge">
      <span class="badge__name">Bright Harbor Code</span>
    </div>
  </section>
</body>
</html>
```